Maple & Fig Business Card FUN & EXCITING

Here is the Information for the Card:
Harvinder Gill (Raj)
E: RajGill@postmeadow.com
C: (480) 730-9146
www.MapleFigLV.com

We don't want traditional Indian cliche, We a playful bold and fun business card.

Files: https://files.cloudvessel.com/folders/7TqRmXa2Lp9KzVb4Hn8YcW3EuJd6FsGo?usp=share_link

https://files.cloudvessel.com/folders/3PzLkQw8Rt5MnXc2Vb7JhY4GsDf9AeUo?usp=share_link

Target Market(s)

Las Vegas Local Restaurant

Industry/Entity Type

Indian Restaurant

Contact Information for Business Card

Name, Email, Cell Phone, Company Logo

```html
<!DOCTYPE html>
<html lang="en">
<head>
<meta charset="utf-8">
<title>Maple &amp; Fig Business Card</title>
<link rel="stylesheet" href="https://fonts.googleapis.com/css2?family=Anton&family=Yellowtail&family=Roboto+Condensed:wght@700&family=Playfair+Display:ital@1&display=swap">
<style>
  :root {
    --stage: #2b2b2b;
    --cream: #fcf6da;
    --ink: #111111;
    --orange: #e99020;
    --orange-dark: #d9761f;
    --pink: #f0457a;
    --rose: #e07aa0;
    --teal: #2bb3a3;
    --social-blue: #3b5aa3;
    --social-pink: #d8236b;
    --social-red: #d42a2a;
  }
  * { box-sizing: border-box; margin: 0; padding: 0; }
  html, body { width: 1200px; height: 689px; overflow: hidden; }
  body { background: var(--stage); position: relative; font-family: "Roboto Condensed", sans-serif; }

  .card { position: absolute; border-radius: 22px; overflow: hidden; background: var(--cream); }

  /* Back of card (portrait) */
  .card--back { left: 60px; top: 82px; width: 300px; height: 525px; background: var(--pink); padding: 20px; }
  .card--back .panel { position: relative; width: 100%; height: 100%; background: var(--cream); border-radius: 26px; overflow: hidden; }
  .card--back .wordmark { position: absolute; top: 34px; left: 0; right: 0; text-align: center; font-family: "Anton", sans-serif; font-size: 50px; line-height: 1; color: var(--ink); letter-spacing: 1px; }
  .card--back .city { position: absolute; top: 98px; left: 0; right: 0; text-align: center; font-family: "Playfair Display", serif; font-style: italic; font-size: 15px; color: var(--ink); }
  .card--back .mascots { position: absolute; top: 130px; left: 30px; width: 200px; height: 170px; border-radius: 18px; background: linear-gradient(160deg, #f6e7c4, #efb16a); }
  .card--back .tagline { position: absolute; top: 312px; left: 0; right: 0; text-align: center; font-family: "Playfair Display", serif; font-style: italic; font-size: 13px; color: var(--ink); }
  .socials { position: absolute; bottom: 36px; left: 0; right: 0; display: flex; justify-content: center; gap: 14px; }
  .social { display: flex; flex-direction: column; align-items: center; gap: 6px; font-size: 11px; color: var(--ink); }
  .social .dot { width: 38px; height: 38px; border-radius: 50%; }
  .social--page .dot { background: var(--social-blue); }
  .social--snap .dot { background: var(--social-pink); }
  .social--dine .dot { background: var(--social-red); }

  /* Front of card (landscape) */
  .card--front { left: 420px; top: 139px; width: 720px; height: 411px; }
  .card--front .sun { position: absolute; inset: 0; }
  .card--front .wordmark { position: absolute; top: 30px; right: 48px; font-family: "Anton", sans-serif; font-size: 62px; line-height: 1; color: var(--ink); letter-spacing: 1px; }
  .card--front .city { position: absolute; top: 104px; right: 52px; font-family: "Playfair Display", serif; font-style: italic; font-size: 16px; color: var(--ink); }
  .card--front .mascots { position: absolute; top: 134px; right: 48px; width: 230px; height: 150px; border-radius: 18px; background: linear-gradient(160deg, #f6e7c4, #efb16a); }
  .card--front .tagline { position: absolute; top: 294px; right: 66px; font-family: "Playfair Display", serif; font-style: italic; font-size: 14px; color: var(--ink); }

  .contact { position: absolute; left: 64px; top: 196px; }
  .contact .name { font-family: "Yellowtail", cursive; font-size: 42px; color: var(--ink); line-height: 1.1; margin-bottom: 14px; }
  .contact ul { list-style: none; }
  .contact li { display: flex; align-items: center; gap: 10px; font-size: 22px; color: var(--ink); line-height: 1.45; }
  .contact svg { width: 22px; height: 22px; flex: none; }
</style>
</head>
<body>

<section class="card card--back">
  <div class="panel">
    <div class="wordmark">Maple &amp; Fig</div>
    <div class="city">Las Vegas, NV</div>
    <div class="mascots" role="img" aria-label="Illustration of a cheerful bowl of curry and a piece of flatbread walking together, with hearts and sparkles"></div>
    <div class="tagline">“A match made in heaven”</div>
    <div class="socials">
      <div class="social social--page"><span class="dot"></span>Pagecircle</div>
      <div class="social social--snap"><span class="dot"></span>Snapframe</div>
      <div class="social social--dine"><span class="dot"></span>Dinerate</div>
    </div>
  </div>
</section>

<section class="card card--front">
  <svg class="sun" viewBox="0 0 720 411" aria-hidden="true">
    <circle cx="290" cy="470" r="322" fill="none" stroke="var(--orange-dark)" stroke-width="6"/>
    <circle cx="290" cy="470" r="308" fill="none" stroke="var(--rose)" stroke-width="10"/>
    <circle cx="290" cy="470" r="294" fill="var(--orange)"/>
  </svg>

  <div class="wordmark">Maple &amp; Fig</div>
  <div class="city">Las Vegas, NV</div>
  <div class="mascots" role="img" aria-label="Illustration of a bowl of curry and a flatbread character pointing, with hearts and sparkles"></div>
  <div class="tagline">“A match made in heaven”</div>

  <div class="contact">
    <div class="name">Harvinder Gill (Raj)</div>
    <ul>
      <li>
        <svg viewBox="0 0 24 24"><circle cx="12" cy="12" r="12" fill="var(--ink)"/><rect x="8.5" y="5" width="7" height="14" rx="1.5" fill="none" stroke="var(--orange)" stroke-width="1.6"/></svg>
        (480) 730-9146
      </li>
      <li>
        <svg viewBox="0 0 24 24"><circle cx="12" cy="12" r="12" fill="var(--ink)"/><rect x="6" y="8" width="12" height="8" fill="none" stroke="var(--orange)" stroke-width="1.6"/><path d="M6 8l6 5 6-5" fill="none" stroke="var(--orange)" stroke-width="1.6"/></svg>
        RajGill@postmeadow.com
      </li>
      <li>
        <svg viewBox="0 0 24 24"><circle cx="12" cy="12" r="12" fill="var(--ink)"/><circle cx="12" cy="12" r="6" fill="none" stroke="var(--orange)" stroke-width="1.6"/><path d="M6 12h12M12 6c-3 3-3 9 0 12M12 6c3 3 3 9 0 12" fill="none" stroke="var(--orange)" stroke-width="1.3"/></svg>
        MapleFigLV.com
      </li>
    </ul>
  </div>
</section>

</body>
</html>
```